Lawn Sign For Construction Projects - Brisk Current

This contest is for a lawn sign that will be placed in the front yard of recently completed construction projects. The goal here is to have a bold advertising sign that is visible from a vehicle driving past.

We are still deciding on the default size for our sign, we also may use multiple sizes. The two sizes we will more than likely be using are: 18"h x 24"w and 24"h x 36"w.

Preference will be given to designers that submit original designs that tie into our current brand and are either in both the size formats listed above or are easy to scale in photoshop or illustrator.

In the files, you will see our logo and an example of a lawn sign.

Please contact us with any questions or comments you may have!

Thank You,
- The Brisk Current Team

Industry/Entity Type

Residential Construction

Colors
34a7d8
ffffff
faa54b

Requirements
Nice to have
• 1. The sign must tie into our current branding and color scheme.
• 2. The sign must be clearly visible and readable.
• 3. The sign must include our phone number in readable print.
• 4. Our website written in small print along the bottom of the sign.
• 5. Must mention we install the following products:
• a.) Solar
• b.) Roofing
• c.) Windows
• d.) Artificial Lawn
• e.) Whole House Fans
• f.) Patio Covers

```html
<!DOCTYPE html>
<html lang="en">
<head>
<meta charset="utf-8">
<title>Brisk Current Lawn Sign</title>
<link href="https://fonts.googleapis.com/css2?family=Montserrat:wght@700&family=Arimo:wght@400&family=Archivo:wght@800&display=swap" rel="stylesheet">
<style>
  :root {
    --sign-black: #000000;
    --brand-orange: #ee7624;
    --brand-blue: #1b75bc;
    --text-white: #ffffff;
  }
  * { margin: 0; padding: 0; box-sizing: border-box; }
  html, body {
    width: 1200px;
    height: 1000px;
    overflow: hidden;
    background: var(--sign-black);
  }
  .lawn-sign {
    position: relative;
    width: 1200px;
    height: 1000px;
    background: var(--sign-black);
    color: var(--text-white);
  }
  .brand-ring {
    position: absolute;
    left: 455px;
    top: 40px;
    width: 290px;
    height: 290px;
  }
  .brand-name {
    position: absolute;
    top: 352px;
    left: 0;
    width: 100%;
    text-align: center;
    font-family: "Montserrat", sans-serif;
    font-weight: 700;
    font-size: 100px;
    line-height: 1;
    letter-spacing: -1px;
    color: var(--brand-blue);
    text-transform: uppercase;
  }
  .phone-number {
    position: absolute;
    top: 475px;
    left: 0;
    width: 100%;
    text-align: center;
    font-family: "Arimo", sans-serif;
    font-weight: 400;
    font-size: 104px;
    line-height: 1;
    letter-spacing: 1px;
  }
  .services-band {
    position: absolute;
    top: 598px;
    left: 0;
    width: 100%;
    height: 232px;
    background: var(--brand-orange);
    display: flex;
    flex-direction: column;
    justify-content: center;
    align-items: center;
    gap: 4px;
  }
  .service-line {
    font-family: "Archivo", sans-serif;
    font-weight: 800;
    font-size: 52px;
    line-height: 60px;
    letter-spacing: 1px;
    white-space: nowrap;
    text-transform: uppercase;
  }
  .website {
    position: absolute;
    top: 860px;
    left: 0;
    width: 100%;
    text-align: center;
    font-family: "Arimo", sans-serif;
    font-weight: 400;
    font-size: 92px;
    line-height: 1;
    letter-spacing: 1px;
  }
</style>
</head>
<body>
  <main class="lawn-sign">
    <svg class="brand-ring" viewBox="0 0 290 290" aria-hidden="true">
      <circle cx="145" cy="145" r="138" fill="none" stroke="var(--brand-orange)" stroke-width="12"/>
    </svg>
    <h1 class="brand-name">Brisk Current</h1>
    <p class="phone-number">555-555-5555</p>
    <section class="services-band">
      <p class="service-line">Solar - Roofing - Windows</p>
      <p class="service-line">Artificial Lawn - Whole House Fans</p>
      <p class="service-line">Patio Covers</p>
    </section>
    <p class="website">websitehere.com</p>
  </main>
</body>
</html>
```